New Design for vehicle wraps

Wanting to redesign our vehicle wraps. I attached current vehicle wrap.

Target Market(s)

Residential and light commercial HVAC

Industry/Entity Type

HVAC

Logo Text

Tellwick Mechanical Inc

```html
<!DOCTYPE html>
<html lang="en">
<head>
<meta charset="utf-8">
<title>Tellwick Mechanical – Vehicle Wrap</title>
<link href="https://fonts.googleapis.com/css2?family=Oswald:wght@500;600;700&display=swap" rel="stylesheet">
<style>
  :root {
    --paper: #ffffff;
    --page: #f2f2f2;
    --brand-green: #2a7a35;
    --flame-orange: #e8682a;
    --cool-blue: #1f56c4;
    --heat-red: #e0301c;
    --ink: #111111;
    --panel-edge: #d6d6d6;
  }
  * { margin: 0; padding: 0; box-sizing: border-box; }
  html, body { width: 869px; height: 1200px; overflow: hidden; background: var(--page); }
  .wrap-sheet {
    width: 869px; height: 1200px;
    display: flex; flex-direction: column; justify-content: space-between;
    padding: 10px 0;
  }
  .wrap-panel { display: block; width: 869px; }
  .wrap-panel--side { height: 380px; }
  .wrap-panel--rear { height: 410px; }
  .body-outline { fill: var(--paper); stroke: var(--panel-edge); stroke-width: 1.5; }
  .cool-field { fill: var(--cool-blue); }
  .heat-field { fill: var(--heat-red); }
  .swoosh-orange { fill: none; stroke: var(--flame-orange); stroke-width: 5; }
  .swoosh-blue { fill: none; stroke: var(--cool-blue); stroke-width: 5; }
  .brand-name { font-family: "Oswald", sans-serif; font-weight: 600; fill: var(--brand-green); letter-spacing: 3px; }
  .brand-sub { font-family: "Oswald", sans-serif; font-weight: 500; fill: var(--flame-orange); letter-spacing: 4px; }
  .phone { font-family: "Oswald", sans-serif; font-weight: 700; fill: var(--ink); }
  .services { font-family: "Oswald", sans-serif; font-weight: 500; fill: var(--brand-green); }
  .services--light { fill: var(--paper); }
  .website { font-family: "Oswald", sans-serif; font-weight: 600; fill: var(--ink); letter-spacing: 1.5px; }
</style>
</head>
<body>
<main class="wrap-sheet">

  <!-- Driver side -->
  <svg class="wrap-panel wrap-panel--side" viewBox="0 0 869 380" aria-label="Driver side wrap panel">
    <rect class="body-outline" x="20" y="50" width="830" height="260" rx="26"/>
    <path class="cool-field" d="M690,51 H824 Q849,51 849,76 V284 Q849,309 824,309 H370 C500,300 620,250 660,200 C690,160 675,110 690,51 Z"/>
    <path class="swoosh-orange" d="M360,300 C480,288 590,245 640,190"/>
    <text class="services" text-anchor="middle" font-size="15">
      <tspan x="285" y="218">RESIDENTIAL-COMMERCIAL</tspan>
      <tspan x="285" y="236">HEATING-COOLING</tspan>
      <tspan x="285" y="254">REPAIR</tspan>
      <tspan x="285" y="272">INSTALLATION</tspan>
    </text>
    <text class="brand-name" x="370" y="135" font-size="44">TELLWICK</text>
    <text class="brand-sub" x="637" y="158" font-size="15" text-anchor="end">MECHANICAL</text>
    <text class="phone" x="500" y="215" font-size="40" text-anchor="middle">661-555-0142</text>
    <text class="website" x="490" y="293" font-size="13" text-anchor="middle">WWW.TELLWICKMECHANICAL.COM</text>
  </svg>

  <!-- Passenger side -->
  <svg class="wrap-panel wrap-panel--side" viewBox="0 0 869 380" aria-label="Passenger side wrap panel">
    <rect class="body-outline" x="20" y="50" width="830" height="260" rx="26"/>
    <path class="heat-field" d="M179,51 H45 Q20,51 20,76 V284 Q20,309 45,309 H499 C369,300 249,250 209,200 C179,160 194,110 179,51 Z"/>
    <path class="swoosh-blue" d="M509,300 C389,288 279,245 229,190"/>
    <text class="brand-name" x="232" y="135" font-size="44">TELLWICK</text>
    <text class="brand-sub" x="499" y="158" font-size="15" text-anchor="end">MECHANICAL</text>
    <text class="phone" x="368" y="215" font-size="40" text-anchor="middle">661-555-0142</text>
    <text class="services" text-anchor="middle" font-size="15">
      <tspan x="585" y="218">RESIDENTIAL-COMMERCIAL</tspan>
      <tspan x="585" y="236">HEATING-COOLING</tspan>
      <tspan x="585" y="254">REPAIR</tspan>
      <tspan x="585" y="272">INSTALLATION</tspan>
    </text>
    <text class="website" x="380" y="293" font-size="13" text-anchor="middle">WWW.TELLWICKMECHANICAL.COM</text>
  </svg>

  <!-- Rear doors -->
  <svg class="wrap-panel wrap-panel--rear" viewBox="0 0 869 410" aria-label="Rear door wrap panel">
    <rect class="body-outline" x="250" y="20" width="370" height="380" rx="30"/>
    <path class="cool-field" d="M251,200 C320,170 380,160 435,160 V399 H280 Q251,399 251,370 Z"/>
    <path class="heat-field" d="M435,160 C490,160 550,170 619,200 V370 Q619,399 590,399 H435 Z"/>
    <text class="brand-name" x="435" y="105" font-size="40" text-anchor="middle">TELLWICK</text>
    <text class="brand-sub" x="545" y="128" font-size="13" text-anchor="end">MECHANICAL</text>
    <text class="phone" x="435" y="218" font-size="38" text-anchor="middle">661-555-0142</text>
    <text class="services services--light" text-anchor="middle" font-size="13">
      <tspan x="345" y="256">RESIDENTIAL-COMMERCIAL</tspan>
      <tspan x="345" y="272">HEATING-COOLING</tspan>
      <tspan x="345" y="288">REPAIR</tspan>
      <tspan x="345" y="304">INSTALLATION</tspan>
    </text>
  </svg>

</main>
</body>
</html>
```